Webdesign für KFZ-Service-Betrieb
Zielgruppe
Wartung, Reparatur und Instandsetzung von Kraftfahrzeugen aller Marken.
Reifenhandel, Old- und Youngtimer-Service, An- und Verkauf von Fahrzeugen.
Aufgabenstellung
Firmenfarbe ist blau.
Moderner, Übersichtlicher und Transparenter Auftritt erwünscht.

```html
<!DOCTYPE html>
<html lang="de">
<head>
<meta charset="utf-8">
<title>Blauwerk KFZ – Wir über uns</title>
<link href="https://fonts.googleapis.com/css2?family=Libre+Baskerville:wght@400;700&family=Open+Sans:wght@400;600&display=swap" rel="stylesheet">
<style>
  :root {
    --brand-blue: #1f2f9c;
    --brand-blue-text: #2a36a8;
    --white: #ffffff;
    --ink-dark: #1d1f24;
    --serif: "Libre Baskerville", Georgia, serif;
    --sans: "Open Sans", Arial, sans-serif;
  }
  html, body { margin: 0; padding: 0; overflow: hidden; background: var(--white); }
  .page { position: relative; width: 1200px; height: 2364px; overflow: hidden; background: var(--white); }

  /* Header */
  .site-header { position: absolute; left: 0; top: 0; width: 1200px; height: 150px; }
  .brand { position: absolute; left: 41px; top: 52px; display: flex; align-items: center; gap: 10px;
           font-family: var(--sans); font-weight: 600; font-size: 22px; letter-spacing: 2px; color: var(--brand-blue); }
  .brand-square { width: 16px; height: 16px; background: var(--brand-blue); }
  .main-nav { position: absolute; left: 0; width: 1200px; top: 82px; text-align: center;
              font-family: var(--sans); font-weight: 600; font-size: 27px; letter-spacing: 5px; color: var(--brand-blue); }

  /* Hero */
  .hero { position: absolute; left: 0; top: 150px; width: 1200px; height: 484px;
          background: linear-gradient(100deg, #6f7c9a 0%, #343c5a 28%, #1b1d26 50%, #303a66 72%, #8c93a6 100%); }
  .hero-claim { position: absolute; left: 0; top: 185px; width: 1200px; margin: 0; text-align: center;
                font-family: var(--sans); font-weight: 600; font-size: 33px; line-height: 59px;
                letter-spacing: 5px; color: var(--white); }

  /* Intro sections */
  .intro { position: absolute; left: 0; width: 1200px; text-align: center; color: var(--brand-blue-text); }
  .intro h2 { margin: 0; font-family: var(--serif); font-weight: 700; font-size: 39px; letter-spacing: 1px; color: var(--brand-blue); }
  .intro p { margin: 14px 0 0; padding: 0 12px; font-family: var(--serif); font-size: 21px; line-height: 29.5px; }
  .intro-pro { top: 710px; }
  .intro-best { top: 1638px; }

  /* Services band */
  .services { position: absolute; left: 0; top: 958px; width: 1200px; height: 599px;
              background: radial-gradient(ellipse at 40% 50%, #6b6659 0%, #3d3b36 45%, #23242a 100%); }
  .service-card { position: absolute; width: 540px; height: 205px; display: flex; }
  .service-text { width: 333px; background: var(--brand-blue); color: var(--white); text-align: center;
                  display: flex; flex-direction: column; justify-content: center; align-items: center; padding: 0 10px; box-sizing: border-box; }
  .service-text h3 { margin: 0 0 6px; font-family: var(--serif); font-weight: 700; font-size: 16.5px; line-height: 22px; }
  .service-text p { margin: 0; font-family: var(--serif); font-size: 9px; line-height: 13px; }
  .read-more { display: inline-block; margin-top: 26px; padding: 5px 9px; background: var(--white);
               color: var(--brand-blue); font-family: var(--serif); font-size: 10px; }
  .service-photo { flex: 1; }
  .card-repair { left: 41px; top: 70px; }
  .card-maintenance { left: 609px; top: 70px; }
  .card-tyres { left: 41px; top: 353px; }
  .card-trade { left: 609px; top: 353px; }
  .photo-repair { background: linear-gradient(135deg, #e3b52a 0%, #2c3a7c 50%, #e7e9ee 100%); }
  .photo-maintenance { background: linear-gradient(135deg, #2a2d36 0%, #3a4a8a 55%, #eceef2 100%); }
  .photo-tyres { background: linear-gradient(135deg, #5f6166 0%, #2b2c30 50%, #d8d9dc 100%); }
  .photo-trade { background: linear-gradient(180deg, #4a4a4a 0%, #b9b9b9 55%, #e6e6e6 100%); }

  /* Contact band */
  .contact { position: absolute; left: 0; top: 1886px; width: 1200px; height: 478px;
             background: linear-gradient(110deg, #15171c 0%, #3a3d45 40%, #2b3560 70%, #4a4c55 100%); color: var(--white); }
  .contact h2 { position: absolute; left: 75px; top: 52px; margin: 0; width: 360px; text-align: center;
                font-family: var(--serif); font-weight: 700; font-size: 66px; line-height: 84px; letter-spacing: 1px; }
  .hours { position: absolute; left: 380px; top: 250px; width: 290px; text-align: center;
           font-family: var(--serif); font-size: 15px; line-height: 27px; }
  .phones { position: absolute; left: 794px; top: 268px; display: flex; align-items: center; gap: 18px; }
  .phones ul { list-style: none; margin: 0; padding: 0; font-family: var(--serif); font-size: 19px; line-height: 27px; }
</style>
</head>
<body>
<div class="page">
  <header class="site-header">
    <div class="brand"><span class="brand-square"></span>Blauwerk KFZ</div>
    <nav class="main-nav">Wir über uns</nav>
  </header>

  <section class="hero" role="img" aria-label="Zwei Mechaniker in blauen Overalls lehnen an einem Auto mit geöffneter Motorhaube">
    <p class="hero-claim">Wartung, Reparatur und Instandsetzung<br>von Kraftfahrzeugen aller Marken.</p>
  </section>

  <section class="intro intro-pro">
    <h2>PRO SOLUTIONS</h2>
    <p>loremp loremp loremp lorem lormel loremp lorem lorem lorem lorem lorem loremp loremp loremp loore lorem lorem&nbsp; lorem lorem lorem&nbsp; loremp loremp loremp loremp loremp lorem lorem loremp loremp loremp lorem lormel loremp lorem lorem lorem lorem&nbsp; lorem loremp loremp loremp loore lorem lorem&nbsp; lorem lorem lorem&nbsp; loremp loremp</p>
  </section>

  <section class="services" role="img" aria-label="Abgedunkelter Hintergrund mit Motorraum eines Fahrzeugs">
    <article class="service-card card-repair">
      <div class="service-text">
        <h3>REPARATUR UND<br>INSTANDSETZUNG</h3>
        <p>Schnelle und zuverlässige Reparaturen für alle Marken, fachgerecht ausgeführt von unserem erfahrenen Team mit modernen Geräten.</p>
        <span class="read-more">Read more</span>
      </div>
      <div class="service-photo photo-repair" role="img" aria-label="Mechaniker mit Kappe arbeitet im Motorraum"></div>
    </article>
    <article class="service-card card-maintenance">
      <div class="service-text">
        <h3>WARTUNG</h3>
        <p>Regelmäßige Inspektion nach Herstellervorgaben, Ölwechsel und Prüfung aller wichtigen Bauteile für Ihre Sicherheit auf der Straße.</p>
        <span class="read-more">Read more</span>
      </div>
      <div class="service-photo photo-maintenance" role="img" aria-label="Mechaniker berät eine Kundin neben einem Fahrzeug"></div>
    </article>
    <article class="service-card card-tyres">
      <div class="service-text">
        <h3>REIFENHANDEL</h3>
        <p>Sommer-, Winter- und Ganzjahresreifen aller Größen, Montage, Auswuchten und Einlagerung zu fairen Preisen direkt bei uns vor Ort.</p>
        <span class="read-more">Read more</span>
      </div>
      <div class="service-photo photo-tyres" role="img" aria-label="Reihe von Reifen auf einer Straße"></div>
    </article>
    <article class="service-card card-trade">
      <div class="service-text">
        <h3>AN- UND VERKAUF<br>VON FAHRZEUGEN</h3>
        <p>Ankauf und Verkauf geprüfter Gebrauchtwagen sowie Old- und Youngtimer, transparent bewertet und ehrlich beraten von Anfang an.</p>
        <span class="read-more">Read more</span>
      </div>
      <div class="service-photo photo-trade" role="img" aria-label="Schwarzweißaufnahme eines klassischen Cabriolets"></div>
    </article>
  </section>

  <section class="intro intro-best">
    <h2>BEST SERVICES</h2>
    <p>loremp loremp loremp lorem lormel loremp lorem lorem lorem lorem lorem loremp loremp loremp loore lorem lorem&nbsp; lorem lorem lorem&nbsp; loremp loremp loremp loremp loremp lorem lorem loremp loremp loremp lorem lormel loremp lorem lorem lorem lorem&nbsp; lorem loremp loremp loremp loore lorem lorem&nbsp; lorem lorem lorem&nbsp; loremp loremp</p>
  </section>

  <section class="contact" role="img" aria-label="Mechaniker mit Klemmbrett im Gespräch mit einer Kundin in der Werkstatt">
    <h2>OUR<br>CONTACT</h2>
    <div class="hours">
      Öffnungszeiten:<br>
      Mo.-Fr.: 07.30 Uhr – 18.00 Uhr<br>
      Sa.: 09.00 Uhr–12.00 Uhr
    </div>
    <div class="phones">
      <svg width="52" height="52" viewBox="0 0 24 24" aria-hidden="true">
        <path fill="#ffffff" d="M6.6 10.8c1.4 2.8 3.8 5.1 6.6 6.6l2.2-2.2c.3-.3.7-.4 1-.2 1.1.4 2.3.6 3.6.6.6 0 1 .4 1 1V20c0 .6-.4 1-1 1C10.6 21 3 13.4 3 4c0-.6.4-1 1-1h3.5c.6 0 1 .4 1 1 0 1.3.2 2.5.6 3.6.1.3 0 .7-.2 1l-2.3 2.2z"/>
      </svg>
      <ul>
        <li>800-5550-1234</li>
        <li>800-5550-1235</li>
      </ul>
    </div>
  </section>
</div>
</body>
</html>
```